High-end residential home builder needs a business card design

We need a new business card design for a small residential construction company based in Boise, Idaho. We specialize in building custom high-end homes and remodels, with a focus on great design and craftsmanship.

We would like to use our current logo, but open to new color suggestions.
Just looking for a clean, sharp, modern design that looks high-end.

Target Market(s)

Upscale clientele

Industry/Entity Type

Contractor

Contact Information for Business Card

Company: Stonefield Custom Builders
Name: Marcus Tilley
Phone number: 208 367 4120
Email: MarcusTilleySCB@mailbox-example.com
Website: Stonefieldcustombuilders-example.com

Font styles to use
Serif
Sans Serif

Requirements
Must have
• Company Logo
Company name
My name
My phone number
My email
Company website
Nice to have
• I have attached a few photos of cards that I really like.

```html
<!DOCTYPE html>
<html lang="en">
<head>
<meta charset="utf-8">
<title>Stonefield Custom Builders — Business Card</title>
<link rel="stylesheet" href="https://fonts.googleapis.com/css2?family=Montserrat:wght@400;600&family=Raleway:wght@600&display=swap">
<style>
  :root {
    --page: #ffffff;
    --card-light: #ffffff;
    --card-dark: #1f1613;
    --ink-dark: #1f1613;
    --ink-light: #ffffff;
    --accent: #e0841f;
    --edge: #e6e9eb;
  }
  * { box-sizing: border-box; margin: 0; padding: 0; }
  html, body {
    width: 1200px; height: 1200px; overflow: hidden;
    background: var(--page);
  }
  .canvas { position: relative; width: 1200px; height: 1200px; }
  .card {
    position: absolute; width: 846px; height: 483px;
    text-align: center;
  }
  .card--front { left: 179px; top: 100px; background: var(--card-light); border: 1px solid var(--edge); }
  .card--back  { left: 185px; top: 634px; background: var(--card-dark); }

  .line { position: absolute; left: 0; right: 0; transform: translateY(-50%); white-space: nowrap; }

  /* front */
  .brand-mark {
    position: absolute; left: 50%; top: 204px;
    width: 70px; height: 70px; transform: translate(-50%, -50%);
    border: 3px solid var(--accent);
  }
  .wordmark {
    font-family: "Raleway", sans-serif; font-weight: 600;
    color: var(--ink-dark); text-transform: uppercase;
  }
  .wordmark--primary { top: 311px; font-size: 24px; letter-spacing: 0.42em; padding-left: 0.42em; }
  .wordmark--secondary { top: 346px; font-size: 14px; letter-spacing: 0.36em; padding-left: 0.36em; }

  /* back */
  .wordmark--on-dark { color: var(--ink-light); }
  .wordmark--badge-top { top: 98px; font-size: 22px; letter-spacing: 0.4em; padding-left: 0.4em; }
  .wordmark--badge-bottom { top: 128px; font-size: 12px; letter-spacing: 0.38em; padding-left: 0.38em; }

  .holder-name {
    top: 235px;
    font-family: "Montserrat", sans-serif; font-weight: 600;
    font-size: 40px; letter-spacing: 0.3em; padding-left: 0.3em;
    color: var(--ink-light); text-transform: uppercase;
  }
  .holder-rule {
    position: absolute; left: 50%; top: 275px;
    width: 171px; height: 2px; transform: translateX(-50%);
    background: var(--ink-light);
  }
  .contact {
    font-family: "Montserrat", sans-serif; font-weight: 400;
    font-size: 12.5px; color: var(--ink-light);
  }
  .contact--company { top: 318px; }
  .contact--reach { top: 347px; }
  .contact--reach .gap { display: inline-block; width: 16px; }
  .contact--web { top: 375px; }
</style>
</head>
<body>
<main class="canvas">
  <section class="card card--front" aria-label="Card front">
    <div class="brand-mark"></div>
    <p class="line wordmark wordmark--primary">Stonefield</p>
    <p class="line wordmark wordmark--secondary">Custom Builders</p>
  </section>

  <section class="card card--back" aria-label="Card back">
    <p class="line wordmark wordmark--on-dark wordmark--badge-top">Stonefield</p>
    <p class="line wordmark wordmark--on-dark wordmark--badge-bottom">Custom Builders</p>
    <h1 class="line holder-name">Marcus Tilley</h1>
    <div class="holder-rule"></div>
    <p class="line contact contact--company">Stonefield Custom Builders</p>
    <p class="line contact contact--reach">Phone&nbsp; 208 367 4120<span class="gap"></span>MarcusTilleySCB@mailbox-example.com</p>
    <p class="line contact contact--web">www.Stonefieldcustombuilders-example.com</p>
  </section>
</main>
</body>
</html>
```